We need a laundry sheet packingbox desgin

-look at our website plooimoes.nl to be in line with our house style/collor
We are a perfume seller and would like to offer also wasshingsheets with NO SMELL, so the customers can buy this incombination with our washingperfumes.
-the wassingheets will be neutrale(NO SMELL)
-it will be for the Dutch market
The next points should be on the desgin of the package
-our brand name: PLOOIMOES
-product name: WASSTRIPS
-(contains) Bevat: 30 wasstrips
-30 wasstrips = 60 wasbeurten
Please take some inspiration of others sellers & regarding eco friendly symbols etc.:
velunta.com & doxamp.nl
Backside information will be provided afther we found the right desgin
Please look at attachement pdf open box.
Here you can find the pdf design where you need to customize:
https://fy.qo/t-Lr8KxPq2Zh

```html
<!DOCTYPE html>
<html lang="nl">
<head>
<meta charset="utf-8">
<title>PLOOIMOES Wasstrips – verpakking dieline</title>
<link href="https://fonts.googleapis.com/css2?family=Cormorant+Garamond:wght@500&family=Montserrat:wght@400;500;600&display=swap" rel="stylesheet">
<style>
  :root {
    --bg: #000000;
    --frame: #3a3a3a;
    --gold: #cc9637;
    --gold-light: #e0b455;
    --cut: #5fbf3f;
    --crease: #c0392b;
    --perf: #e53935;
    --window: #3a8fa0;
    --strip: #cfcfcf;
    --white: #ffffff;
  }
  html, body {
    margin: 0;
    padding: 0;
    width: 1200px;
    height: 974px;
    overflow: hidden;
    background: var(--bg);
  }
  .dieline {
    display: block;
    width: 1200px;
    height: 974px;
  }
  .sheet-frame { fill: var(--bg); stroke: var(--frame); stroke-width: 4; }
  .cut { fill: var(--bg); stroke: var(--cut); stroke-width: 1.6; }
  .panel { fill: var(--bg); stroke: var(--crease); stroke-width: 1.4; }
  .panel--gold { fill: var(--gold); }
  .tuck { fill: var(--gold); stroke: var(--cut); stroke-width: 1.6; }
  .tape-strip { fill: var(--strip); }
  .perforation { stroke: var(--perf); stroke-width: 1.6; stroke-dasharray: 8 6; }
  .window-cut { fill: none; stroke: var(--window); stroke-width: 1.6; }
  .window-fold { fill: none; stroke: var(--perf); stroke-width: 1.6; stroke-dasharray: 8 6; }
  .window-ticks { stroke: #4a4fb0; stroke-width: 3; }
  .brand-serif {
    font-family: "Cormorant Garamond", Georgia, serif;
    font-weight: 500;
    letter-spacing: 1px;
  }
  .brand-serif--dark { fill: #111111; font-size: 22px; }
  .brand-serif--gold { fill: var(--gold); font-size: 19px; }
  .product-title {
    font-family: "Montserrat", Arial, sans-serif;
    font-weight: 500;
    fill: var(--white);
    font-size: 66px;
  }
  .icon-line { fill: none; stroke: var(--gold); stroke-width: 2.4; }
  .icon-caption {
    font-family: "Montserrat", Arial, sans-serif;
    fill: var(--gold-light);
    font-size: 6.5px;
  }
  .count-pill { fill: var(--gold); }
  .count-label {
    font-family: "Montserrat", Arial, sans-serif;
    font-weight: 500;
    fill: #111111;
    font-size: 12px;
  }
  .count-sub {
    font-family: "Montserrat", Arial, sans-serif;
    font-weight: 600;
    fill: #111111;
    font-size: 5px;
  }
</style>
</head>
<body>
<svg class="dieline" viewBox="0 0 2140 1736" xmlns="http://www.w3.org/2000/svg">
  <defs>
    <radialGradient id="halftone-glow" cx="0.6" cy="0.45" r="0.6">
      <stop offset="0" stop-color="#2a2a2a"/>
      <stop offset="1" stop-color="#000000" stop-opacity="0"/>
    </radialGradient>
    <radialGradient id="halftone-glow-gold" cx="0.2" cy="0.4" r="0.7">
      <stop offset="0" stop-color="#b8842e"/>
      <stop offset="1" stop-color="#cc9637" stop-opacity="0"/>
    </radialGradient>
  </defs>

  <rect class="sheet-frame" x="2" y="2" width="2136" height="1732"/>

  <!-- Side flap (glue side) -->
  <g class="side-flap">
    <path class="cut" d="M300,474 L310,362 Q311,355 318,355 H402 Q409,355 410,362 L420,474 Z"/>
    <path class="cut" d="M300,1262 L310,1375 Q311,1382 318,1382 H402 Q409,1382 410,1375 L420,1262 Z"/>
    <rect class="panel" x="300" y="474" width="126" height="788" style="stroke:var(--cut)"/>
    <line x1="426" y1="474" x2="426" y2="1262" stroke="var(--crease)" stroke-width="1.4"/>
    <path class="cut" d="M382,818 L396,828 V908 L382,918 Z"/>
  </g>

  <!-- Back panel -->
  <g class="back-panel">
    <path class="cut" d="M430,470 L437,362 Q438,355 446,355 H982 Q990,355 991,362 L998,470 Z"/>
    <rect class="tape-strip" x="456" y="381" width="516" height="71"/>
    <g class="perforation">
      <line x1="469" y1="386" x2="469" y2="447"/><line x1="507" y1="386" x2="507" y2="447"/>
      <line x1="545" y1="386" x2="545" y2="447"/><line x1="583" y1="386" x2="583" y2="447"/>
      <line x1="621" y1="386" x2="621" y2="447"/><line x1="659" y1="386" x2="659" y2="447"/>
      <line x1="697" y1="386" x2="697" y2="447"/><line x1="735" y1="386" x2="735" y2="447"/>
      <line x1="773" y1="386" x2="773" y2="447"/><line x1="811" y1="386" x2="811" y2="447"/>
      <line x1="849" y1="386" x2="849" y2="447"/><line x1="887" y1="386" x2="887" y2="447"/>
      <line x1="925" y1="386" x2="925" y2="447"/><line x1="962" y1="386" x2="962" y2="447"/>
    </g>
    <path class="cut" d="M430,1266 L437,1375 Q438,1382 446,1382 H982 Q990,1382 991,1375 L998,1266 Z"/>
    <rect class="tape-strip" x="460" y="1291" width="516" height="61"/>
    <g class="perforation">
      <line x1="473" y1="1294" x2="473" y2="1350"/><line x1="511" y1="1294" x2="511" y2="1350"/>
      <line x1="549" y1="1294" x2="549" y2="1350"/><line x1="587" y1="1294" x2="587" y2="1350"/>
      <line x1="625" y1="1294" x2="625" y2="1350"/><line x1="663" y1="1294" x2="663" y2="1350"/>
      <line x1="701" y1="1294" x2="701" y2="1350"/><line x1="739" y1="1294" x2="739" y2="1350"/>
      <line x1="777" y1="1294" x2="777" y2="1350"/><line x1="815" y1="1294" x2="815" y2="1350"/>
      <line x1="853" y1="1294" x2="853" y2="1350"/><line x1="891" y1="1294" x2="891" y2="1350"/>
      <line x1="929" y1="1294" x2="929" y2="1350"/><line x1="966" y1="1294" x2="966" y2="1350"/>
    </g>
    <rect class="panel" x="426" y="470" width="577" height="796"/>
  </g>

  <!-- Spine panel -->
  <g class="spine-panel">
    <path class="cut" d="M1008,470 L1019,362 Q1020,355 1027,355 H1109 Q1116,355 1117,362 L1128,470 Z"/>
    <path class="cut" d="M1008,1266 L1019,1375 Q1020,1382 1027,1382 H1109 Q1116,1382 1117,1375 L1128,1266 Z"/>
    <rect class="panel panel--gold" x="1003" y="474" width="130" height="788"/>
    <circle cx="1068" cy="808" r="11" fill="#111111"/>
    <text class="brand-serif brand-serif--dark" transform="translate(1061,835) rotate(90)" textLength="104">PLOOIMOES</text>
  </g>

  <!-- Front panel -->
  <g class="front-panel">
    <path class="cut" d="M1138,470 L1145,353 Q1146,346 1154,346 H1690 Q1699,346 1700,353 L1708,470 Z"/>
    <path class="cut" d="M1138,1266 L1145,1383 Q1146,1390 1154,1390 H1690 Q1699,1390 1700,1383 L1708,1266 Z"/>
    <rect class="panel" x="1133" y="470" width="580" height="796"/>
    <rect x="1470" y="470" width="243" height="290" fill="url(#halftone-glow)" role="img" aria-label="Halftone dot pattern fading into the dark front"/>

    <!-- Tuck flap -->
    <path class="tuck" d="M1713,474 H1803 Q1838,474 1838,509 V1227 Q1838,1262 1803,1262 H1713 Z"/>
    <rect x="1713" y="474" width="95" height="260" fill="url(#halftone-glow-gold)" role="img" aria-label="Halftone dot pattern on gold tuck flap"/>
    <line x1="1713" y1="474" x2="1713" y2="1262" stroke="var(--crease)" stroke-width="1.4"/>
    <line x1="1805" y1="660" x2="1805" y2="1080" stroke="var(--crease)" stroke-width="1.2"/>
    <path d="M1806,834 A35,35 0 0 0 1806,902" fill="none" stroke="var(--cut)" stroke-width="1.6"/>
    <text class="brand-serif brand-serif--dark" transform="translate(1776,902) rotate(-90)" textLength="104">PLOOIMOES</text>
    <circle cx="1768" cy="928" r="11" fill="#111111"/>

    <!-- Window cut-out -->
    <path class="window-cut" d="M1232,569 H1745 C1770,569 1780,585 1790,610 L1805,660 V1080 L1790,1130 C1780,1155 1770,1167 1745,1167 H1232 Q1219,1167 1219,1154 V582 Q1219,569 1232,569 Z"/>
    <path class="window-fold" d="M1268,575 H1745 C1765,575 1775,590 1785,612"/>
    <path class="window-fold" d="M1268,1161 H1745 C1765,1161 1775,1146 1785,1124"/>
    <g class="window-ticks">
      <line x1="1268" y1="565" x2="1268" y2="580"/><line x1="1268" y1="1156" x2="1268" y2="1171"/>
      <line x1="1788" y1="603" x2="1792" y2="598"/><line x1="1790" y1="622" x2="1795" y2="618"/>
      <line x1="1797" y1="640" x2="1802" y2="636"/><line x1="1817" y1="660" x2="1817" y2="668"/>
      <line x1="1828" y1="660" x2="1828" y2="668"/><line x1="1817" y1="1076" x2="1817" y2="1084"/>
      <line x1="1828" y1="1076" x2="1828" y2="1084"/><line x1="1797" y1="1104" x2="1802" y2="1108"/>
      <line x1="1790" y1="1122" x2="1795" y2="1126"/><line x1="1788" y1="1136" x2="1792" y2="1140"/>
    </g>

    <!-- Brand -->
    <circle cx="1317" cy="858" r="32" fill="var(--gold)"/>
    <text class="brand-serif brand-serif--gold" transform="translate(1380,908) rotate(-90)" textLength="100">PLOOIMOES</text>

    <!-- Product name -->
    <text class="product-title" transform="translate(1447,1100) rotate(-90)" textLength="365" lengthAdjust="spacingAndGlyphs">WASSTRIPS</text>
    <circle cx="1425" cy="678" r="43" fill="var(--white)" role="img" aria-label="Illustration of a laundry sheet"/>

    <!-- Washing machine icon -->
    <g class="icon-line">
      <rect x="1525" y="709" width="96" height="77" rx="6"/>
      <circle cx="1580" cy="747" r="27"/>
      <circle cx="1580" cy="747" r="19"/>
      <rect x="1529" y="757" width="8" height="20" rx="2"/>
      <line x1="1533" y1="716" x2="1533" y2="740" stroke-dasharray="4 5"/>
    </g>
    <rect x="1570" y="792" width="51" height="48" fill="var(--gold)" opacity="0.85" role="img" aria-label="Illustration of a laundry basket with bubbles"/>

    <!-- Feature icons -->
    <circle class="icon-line" cx="1543" cy="924" r="18"/>
    <circle class="icon-line" cx="1543" cy="983" r="18"/>
    <circle cx="1543" cy="954" r="2" fill="var(--gold)"/>
    <text class="icon-caption" transform="translate(1572,945) rotate(-90)">Neutraal</text>
    <text class="icon-caption" transform="translate(1580,945) rotate(-90)">(Geen Geur)</text>
    <text class="icon-caption" transform="translate(1572,1000) rotate(-90)">Voor alle</text>
    <text class="icon-caption" transform="translate(1580,1003) rotate(-90)">kledingtypes</text>

    <!-- Count -->
    <rect class="count-pill" x="1594" y="880" width="18" height="147" rx="9"/>
    <rect x="1610" y="890" width="11" height="128" rx="3" fill="var(--white)"/>
    <text class="count-label" transform="translate(1607,1018) rotate(-90)" textLength="132">Bevat 30 wasstrips</text>
    <text class="count-sub" transform="translate(1618,1012) rotate(-90)" textLength="112">30 WASSTRIPS = 60 WASBEURTEN</text>
  </g>
</svg>
</body>
</html>
```